business card for training & coaching company, Brightwell.co

Create a warm, clean, professional 2-sided business card for Brightwell.co.
Brightwell.co is a new company that shares Brightwell Dialogue (combination of mindfulness, kindness, and nonviolent communication), training and coaching individuals and groups.
Include the logo provided, perhaps incorporating a second opaque version of it as well.
Feelings & Needs lists on the reverse side of the card.

Target Market(s)

Women 30-60 years old, university educated.
Spiritual, may be Buddhist.

Industry/Entity Type

Training

Contact Information for Business Card

Marisabel T. Oberholt, MSc
Group Facilitator & Certified Wellness Coach
Brightwell Dialogue training & support
Group Facilitator & Coach
01632 960 418
07700 900 862
www.brightwell-example.co

Font styles to use
Sans Serif

Requirements
Must have
• Front -- Contact details, logo provided.
• Back -- Feelings list; Needs list
• Professional yet warm, inviting, friendly feel.
Nice to have
• little graphics (telephone for phone number, envelope for email, globe for web);
• Clean font (like Sathu, Frutiga, Helvetica).
• Feeling of movement or transformation.
Should not have
• More than 3 colours.
• Loud or busy designs.
• A gentle curve or two is ok, but not swirly designs.
• No black or other heavy backgrounds.

```html
<!DOCTYPE html>
<html lang="en">
<head>
<meta charset="utf-8">
<title>Brightwell.co business card</title>
<link href="https://fonts.googleapis.com/css2?family=Open+Sans:wght@300;400;600&display=swap" rel="stylesheet">
<style>
  :root {
    --orange: #f0711f;
    --orange-soft: #f6a04d;
    --cream: #fdfaf1;
    --cream-warm: #f7efcf;
    --gold: #f1e19a;
    --stage: #ece9e4;
    --white: #ffffff;
  }
  * { box-sizing: border-box; margin: 0; padding: 0; }
  html, body { width: 1200px; height: 1000px; overflow: hidden; }
  body {
    background: var(--stage);
    font-family: "Open Sans", Arial, sans-serif;
    color: var(--orange);
    position: relative;
  }
  .card {
    position: absolute;
    top: 325px;
    width: 540px;
    height: 350px;
    background: linear-gradient(160deg, var(--white) 0%, var(--cream) 55%, var(--cream-warm) 100%);
    box-shadow: 0 6px 18px rgba(0,0,0,0.12);
    overflow: hidden;
  }
  .card--front { left: 40px; }
  .card--back { left: 620px; }
  .card__waves { position: absolute; inset: 0; width: 100%; height: 100%; }

  /* Front */
  .brand-mark {
    position: absolute;
    left: 40px; top: 110px;
    width: 150px; height: 150px;
    border-radius: 50%;
    background: radial-gradient(circle at 40% 40%, var(--orange-soft), var(--orange));
  }
  .front-text {
    position: absolute;
    right: 78px; top: 36px;
    text-align: right;
  }
  .brand-name { font-weight: 300; font-size: 40px; line-height: 1; letter-spacing: -0.5px; }
  .brand-sub { font-weight: 400; font-size: 15px; margin-top: 2px; }
  .person { font-weight: 400; font-size: 20px; margin-top: 34px; }
  .person small { font-size: 11px; }
  .role { font-weight: 400; font-size: 10.5px; line-height: 1.45; margin-top: 2px; }
  .contact { font-weight: 400; font-size: 12.5px; line-height: 1; }
  .contact-list { position: absolute; right: 78px; top: 224px; text-align: right; }
  .contact-list .contact { height: 22px; line-height: 22px; }
  .icon-rail {
    position: absolute;
    right: 30px; top: 224px;
    width: 40px;
  }
  .icon-tab {
    display: flex; align-items: center; justify-content: center;
    height: 20px; margin-bottom: 2px;
    background: var(--orange);
  }
  .icon-tab svg { width: 13px; height: 13px; }
  .rail-bar {
    position: absolute; right: 30px; top: 196px;
    width: 40px; height: 24px; background: var(--orange);
  }

  /* Back */
  .back-brand {
    position: absolute; left: 30px; top: 92px;
    display: flex; align-items: center; gap: 10px;
  }
  .back-brand .dot {
    width: 56px; height: 56px; border-radius: 50%;
    background: radial-gradient(circle at 40% 40%, var(--orange-soft), var(--orange));
  }
  .back-brand .brand-name { font-size: 30px; }
  .back-brand .brand-sub { font-size: 12px; }
  .list-block { position: absolute; }
  .list-block--needs { left: 290px; top: 24px; }
  .list-block--feelings { left: 30px; top: 184px; }
  .list-band {
    background: var(--orange); color: var(--white);
    font-weight: 400; font-size: 14px; letter-spacing: 1px;
    text-align: center; padding: 2px 0; width: 140px;
  }
  .list-columns { display: flex; gap: 26px; margin-top: 6px; padding-left: 6px; }
  .list-columns ul { list-style: none; }
  .list-columns li { font-size: 14px; line-height: 1.3; font-weight: 400; white-space: nowrap; }
  .list-columns li::before { content: "•"; color: var(--orange); margin-right: 6px; font-size: 11px; }
</style>
</head>
<body>

<section class="card card--front" aria-label="Front of card">
  <svg class="card__waves" viewBox="0 0 540 350" preserveAspectRatio="none" aria-hidden="true">
    <path d="M0 350 C160 300 330 250 540 120 L540 350 Z" fill="var(--gold)" opacity="0.35"/>
    <path d="M0 350 C200 320 360 280 540 180" stroke="var(--white)" stroke-width="3" fill="none" opacity="0.9"/>
    <path d="M60 350 C240 310 400 250 540 150" stroke="var(--gold)" stroke-width="1.5" fill="none" opacity="0.7"/>
  </svg>

  <div class="brand-mark" aria-hidden="true"></div>

  <div class="front-text">
    <div class="brand-name">Brightwell.co</div>
    <div class="brand-sub">Brightwell Dialogue</div>
    <div class="person">Marisabel T. Oberholt<small>, MSc</small></div>
    <div class="role">Group Facilitator &amp; Certified Wellness Coach<br>Brightwell Dialogue Training &amp; Support</div>
  </div>

  <div class="contact-list">
    <div class="contact">01632 960 418 / 07700 900 862</div>
    <div class="contact">info@brightwell-example.co</div>
    <div class="contact">www.brightwell-example.co</div>
  </div>

  <div class="icon-rail">
    <div class="icon-tab" aria-label="Phone">
      <svg viewBox="0 0 16 16"><path d="M4 1.5 L6.5 4.5 L5 6 C6 8.5 7.5 10 10 11 L11.5 9.5 L14.5 12 L12.5 14.5 C7 14 2 9 1.5 3.5 Z" fill="var(--white)"/></svg>
    </div>
    <div class="icon-tab" aria-label="Email">
      <svg viewBox="0 0 16 16"><rect x="1.5" y="3.5" width="13" height="9" fill="none" stroke="var(--white)" stroke-width="1.5"/><path d="M1.5 3.5 L8 9 L14.5 3.5" fill="none" stroke="var(--white)" stroke-width="1.5"/></svg>
    </div>
    <div class="icon-tab" aria-label="Website">
      <svg viewBox="0 0 16 16"><circle cx="8" cy="8" r="6.5" fill="none" stroke="var(--white)" stroke-width="1.3"/><ellipse cx="8" cy="8" rx="3" ry="6.5" fill="none" stroke="var(--white)" stroke-width="1.1"/><path d="M1.5 8 H14.5" stroke="var(--white)" stroke-width="1.1"/></svg>
    </div>
  </div>
  <div class="rail-bar" aria-hidden="true"></div>
</section>

<section class="card card--back" aria-label="Back of card">
  <svg class="card__waves" viewBox="0 0 540 350" preserveAspectRatio="none" aria-hidden="true">
    <path d="M300 350 C420 300 500 200 540 60 L540 350 Z" fill="var(--gold)" opacity="0.35"/>
    <path d="M260 350 C400 300 490 200 540 80" stroke="var(--white)" stroke-width="3" fill="none" opacity="0.9"/>
    <path d="M330 350 C440 290 510 190 540 110" stroke="var(--gold)" stroke-width="1.5" fill="none" opacity="0.7"/>
  </svg>

  <div class="back-brand">
    <div class="dot" aria-hidden="true"></div>
    <div>
      <div class="brand-name">Brightwell.co</div>
      <div class="brand-sub">Brightwell Dialogue</div>
    </div>
  </div>

  <div class="list-block list-block--needs">
    <div class="list-band">NEEDS</div>
    <div class="list-columns">
      <ul><li>belonging</li><li>choice</li><li>charity</li><li>empathy</li><li>freedom</li><li>meaning</li></ul>
      <ul><li>mourning</li><li>peace</li><li>safety</li><li>support</li><li>understanding</li><li>&amp; more...</li></ul>
    </div>
  </div>

  <div class="list-block list-block--feelings">
    <div class="list-band">FEELINGS</div>
    <div class="list-columns">
      <ul><li>confusion</li><li>curious</li><li>despair</li><li>edgy</li><li>fiery</li><li>grief</li></ul>
      <ul><li>nervous</li><li>powerless</li><li>shock</li><li>torn</li><li>weary</li><li>&amp; more...</li></ul>
    </div>
  </div>
</section>

</body>
</html>
```